Window Cleaning Flyer targeting body corporates

Need a flyer for window cleaning targeting body corporate (approx A5 print size). It should be professional and match the logo attached.
We are looking to standout but not be to over the top for a window cleaning/services company.
We want to entice the receptionist or managers to call us because they see no good reason not to.

Industry/Entity Type

Window Cleaning

Font styles to use
Serif

Colors
0555a3
fbed22

Requirements
Must have
• Professional with a few of the photos attached included. Must include logo and the following contact details:
• Ph: 9413 6570
• email: admin@brightpaneworks.com.au
• PO Box 4726
• Marlowe Heights
• 3284
Nice to have
• Colours matching logo/ van print layout. Looking for more of a simplistic professional design.
Should not have
• Cartoon pictures, animated decorations or stock photos.

```html
<!DOCTYPE html>
<html lang="en">
<head>
<meta charset="utf-8">
<title>Brightpane Window Cleaning – Body Corporate Flyer</title>
<link rel="stylesheet" href="https://fonts.googleapis.com/css2?family=Roboto:wght@400;500;700;900&display=swap">
<style>
  :root {
    --yellow: #fbed22;
    --navy: #04578b;
    --blue: #0a70bd;
    --blue-light: #4b9ad6;
    --charcoal: #2c3640;
    --ink: #222a31;
    --white: #ffffff;
    --page: #d4d4d4;
  }
  html, body {
    margin: 0;
    padding: 0;
    width: 1041px;
    height: 1200px;
    overflow: hidden;
    background: var(--page);
    font-family: "Roboto", Arial, sans-serif;
  }
  .canvas {
    position: relative;
    width: 1041px;
    height: 1200px;
    overflow: hidden;
  }
  .flyer {
    position: absolute;
    left: 96px;
    top: 0;
    width: 765px;
    height: 1082px;
    background: var(--white);
    transform: scale(1.1091);
    transform-origin: 0 0;
    overflow: hidden;
  }
  .hero {
    position: absolute;
    left: 0; top: 0;
    width: 765px; height: 646px;
  }
  .hero svg { position: absolute; left: 0; top: 0; }
  .brand {
    position: absolute;
    left: 398px; top: 124px;
    width: 360px;
    text-align: center;
    color: var(--yellow);
    font-weight: 900;
  }
  .brand-name {
    font-size: 50px;
    letter-spacing: 1px;
    line-height: 1;
  }
  .brand-tag {
    margin-top: 22px;
    font-size: 27px;
    letter-spacing: 2px;
    line-height: 1;
  }
  .services {
    position: absolute;
    left: 0; top: 498px;
    width: 765px; height: 147px;
  }
  .service {
    position: absolute;
    top: 0;
    width: 205px; height: 147px;
    background: var(--blue);
    color: var(--white);
    text-align: center;
    box-sizing: border-box;
    padding-top: 32px;
  }
  .service::before, .service::after {
    content: "";
    position: absolute;
    top: 8px; bottom: 18px;
    width: 7px;
    background: var(--blue-light);
  }
  .service::before { left: 0; }
  .service::after { right: 0; }
  .service-base {
    position: absolute;
    left: 0; right: 0; bottom: 0;
    height: 18px;
    background: var(--charcoal);
  }
  .service-title {
    font-weight: 700;
    font-size: 21px;
    line-height: 20px;
  }
  .service-note {
    font-size: 12px;
    line-height: 13px;
    margin-top: 3px;
  }
  .service--window { left: 27px; }
  .service--gutter { left: 280px; }
  .service--pressure { left: 533px; }
  .pitch {
    position: absolute;
    left: 42px; top: 682px;
    width: 690px;
    color: var(--ink);
  }
  .pitch-heading {
    margin: 0;
    font-weight: 400;
    font-size: 30px;
    line-height: 37px;
  }
  .pitch-heading strong {
    display: block;
    color: var(--blue);
    font-weight: 700;
  }
  .pitch p {
    margin: 4px 0 0;
    font-size: 14px;
    line-height: 24px;
  }
  .pitch ul {
    list-style: none;
    margin: 12px 0 0;
    padding: 0;
    font-size: 14px;
    line-height: 24px;
  }
  .pitch li {
    position: relative;
    padding-left: 20px;
  }
  .pitch li::before {
    content: "";
    position: absolute;
    left: 1px; top: 7px;
    border-left: 8px solid var(--ink);
    border-top: 5px solid transparent;
    border-bottom: 5px solid transparent;
  }
  .pitch .pitch-close { margin-top: 4px; }
  .rule {
    position: absolute;
    left: 0; top: 975px;
    width: 765px; height: 12px;
    background: var(--charcoal);
  }
  .footer {
    position: absolute;
    left: 0; top: 992px;
    width: 765px; height: 90px;
    background: var(--blue);
  }
  .cta {
    position: absolute;
    left: 43px; top: 951px;
    width: 338px; height: 82px;
    background: var(--charcoal);
    color: var(--white);
    text-align: center;
    font-size: 18px;
    line-height: 23px;
    box-sizing: border-box;
    padding-top: 17px;
    box-shadow: 0 6px 8px rgba(0,0,0,0.35);
  }
  .contact {
    position: absolute;
    right: 48px; top: 1000px;
    color: var(--white);
    text-align: right;
    font-size: 14px;
    line-height: 17.7px;
    font-style: normal;
  }
</style>
</head>
<body>
<div class="canvas">
  <div class="flyer">
    <section class="hero">
      <svg width="765" height="646" viewBox="0 0 765 646" aria-hidden="false">
        <defs>
          <linearGradient id="photoFacade" x1="0" y1="0" x2="1" y2="1">
            <stop offset="0" stop-color="#8a6a4e"/>
            <stop offset="0.6" stop-color="#4d4a48"/>
            <stop offset="1" stop-color="#6f8a55"/>
          </linearGradient>
          <linearGradient id="photoPool" x1="0" y1="0" x2="1" y2="1">
            <stop offset="0" stop-color="#b9c4cc"/>
            <stop offset="0.5" stop-color="#4e5c66"/>
            <stop offset="1" stop-color="#1f2a30"/>
          </linearGradient>
          <linearGradient id="photoCrew" x1="0" y1="0" x2="1" y2="1">
            <stop offset="0" stop-color="#7d8893"/>
            <stop offset="0.5" stop-color="#2a313a"/>
            <stop offset="1" stop-color="#1c232b"/>
          </linearGradient>
        </defs>
        <rect class="hero-yellow" x="0" y="0" width="765" height="646" fill="var(--yellow)"/>
        <polygon class="hero-panel-edge" points="484,0 765,0 765,388 655,498 622,498 296,185" fill="var(--white)"/>
        <polygon class="hero-panel" points="498,0 765,0 765,400 667,498 628,498 312,185" fill="var(--navy)"/>
        <rect class="service-band" x="0" y="525" width="765" height="121" fill="var(--blue)"/>
        <polygon role="img" aria-label="Photo: cleaner washing the timber-slatted facade of an apartment building with a water-fed pole" points="258,172 362,276 258,380 154,276" fill="url(#photoFacade)"/>
        <polygon role="img" aria-label="Photo: cleaner standing in a pond washing glass panels with a long pole" points="148,288 250,390 148,492 46,390" fill="url(#photoPool)"/>
        <polygon role="img" aria-label="Photo: two uniformed team members cleaning a shopfront window" points="371,285 473,387 371,489 269,387" fill="url(#photoCrew)"/>
      </svg>
      <div class="brand">
        <div class="brand-name">BRIGHTPANE</div>
        <div class="brand-tag">WINDOW CLEANING</div>
      </div>
      <div class="services">
        <div class="service service--window">
          <div class="service-title">WINDOW<br>CLEANING</div>
          <div class="service-base"></div>
        </div>
        <div class="service service--gutter">
          <div class="service-title">GUTTER<br>CLEANING</div>
          <div class="service-note">using our ladder free<br>gutter vacuum</div>
          <div class="service-base"></div>
        </div>
        <div class="service service--pressure">
          <div class="service-title">PRESSURE<br>WASHING</div>
          <div class="service-note">including moss treatment<br>to prevent mould regrowth<br>on concrete surface</div>
          <div class="service-base"></div>
        </div>
      </div>
    </section>

    <section class="pitch">
      <h1 class="pitch-heading">LET BRIGHTPANE TAKE CARE OF YOUR <strong>BODY CORPORATE NEEDS!</strong></h1>
      <p>With over 15 years of experience we will ensure the job is completed to the highest standard everytime..<br>Brightpane specialises in Body Corporate:</p>
      <ul>
        <li>Window Cleaning</li>
        <li>Gutter Cleaning (using our ladder free gutter vacuum)</li>
        <li>Pressure Washing including moss treatment to prevent mould regrowth on concrete surface</li>
      </ul>
      <p class="pitch-close">Most Importantly, Brightpane Window Cleaning take pride in being friendly and courteous to all residents.</p>
    </section>

    <div class="rule"></div>
    <footer class="footer"></footer>
    <div class="cta">Contact the Brightpane Team for an easy,<br>FREE quote today!</div>
    <address class="contact">
      Ph: 9413 6570<br>
      admin@brightpaneworks.com.au<br>
      PO Box 4726<br>
      Marlowe Heights 3284
    </address>
  </div>
</div>
</body>
</html>
```